Invitation For Service Management Event

We need an invitation for clients to an event on the platform service Management. This has to be appealing and needs to be "tech" inspired. it is important that the design of the invitation is as clean as possible. I attached some images so that you understand the kind of enviorment we want to portray in the invitation.
- I also attached our company logo to the brief under the file Pelvunko Transparent. The logo has to be in the invitation.

```html
<!DOCTYPE html>
<html lang="es">
<head>
<meta charset="utf-8">
<title>Platform Service Management – Invitación</title>
<link rel="stylesheet" href="https://fonts.googleapis.com/css2?family=Montserrat:wght@400;500;600;700&display=swap">
<style>
  :root{
    --night:#0b1016;
    --steel:#1c2730;
    --glow:#6cc6ec;
    --glow-deep:#1d8fd0;
    --ink:#111418;
    --paper:#f7f8fa;
    --brand-red:#e0382b;
    --white:#ffffff;
  }
  *{margin:0;padding:0;box-sizing:border-box}
  html,body{width:857px;height:1200px;overflow:hidden;background:var(--paper)}
  body{font-family:"Montserrat",Arial,sans-serif;color:var(--ink)}
  .invitation{position:relative;width:857px;height:1200px;background:var(--paper)}
  .hero{position:absolute;left:0;top:0;width:857px;height:600px;overflow:hidden}
  .hero-backdrop{position:absolute;inset:0;
    background:
      radial-gradient(ellipse 45% 40% at 50% 48%, rgba(40,150,220,.55), transparent 70%),
      radial-gradient(ellipse 70% 60% at 50% 50%, #2c3a44 0%, #141c23 60%, var(--night) 100%);}
  .emblem{position:absolute;left:0;top:0}
  .hero-text{position:absolute;left:0;top:0;width:857px;text-align:center;color:var(--white)}
  .kicker{position:absolute;top:198px;width:100%;font-size:17px;font-weight:500}
  .event-title{position:absolute;top:228px;width:100%;font-size:42px;font-weight:400;line-height:44px;color:var(--glow);letter-spacing:.5px}
  .brand{position:absolute;top:668px;left:0;width:857px;display:flex;justify-content:center;align-items:center;gap:14px}
  .brand-dot{width:54px;height:54px;border-radius:50%;background:var(--brand-red)}
  .brand-name{font-size:36px;font-weight:700;color:var(--ink);line-height:1}
  .brand-tagline{display:block;font-size:12px;font-weight:600;color:var(--brand-red);margin-top:4px;letter-spacing:.2px}
  .when{position:absolute;top:792px;width:100%;text-align:center;font-size:24px;font-weight:600;line-height:32px}
  .agenda{position:absolute;top:912px;width:100%;text-align:center;font-size:16.5px;line-height:23px}
  .rsvp{position:absolute;top:1016px;width:100%;text-align:center;font-size:18px;line-height:23.5px}
  .rsvp strong{font-weight:600}
  .footer-band{position:absolute;left:0;bottom:0;width:857px;height:14px;background:var(--ink)}
</style>
</head>
<body>
<main class="invitation">
  <section class="hero">
    <div class="hero-backdrop" role="img" aria-label="Dark circuit-board background with hexagon grid and glowing blue traces"></div>
    <svg class="emblem" width="857" height="600" viewBox="0 0 857 600">
      <circle cx="428" cy="293" r="222" fill="none" stroke="var(--glow)" stroke-width="18"
        stroke-dasharray="1046 1395" transform="rotate(-90 428 293)" opacity=".95"/>
      <circle cx="428" cy="293" r="208" fill="#07090c"/>
      <circle cx="428" cy="293" r="172" fill="none" stroke="var(--glow-deep)" stroke-width="1.2" opacity=".8"/>
    </svg>
    <div class="hero-text">
      <p class="kicker">Come and join us</p>
      <h1 class="event-title">PLATFORM<br>SERVICE<br>MANAGEMENT</h1>
    </div>
  </section>

  <div class="brand">
    <span class="brand-dot"></span>
    <div>
      <span class="brand-name">PELVUNKO</span>
      <span class="brand-tagline">IT CONSULTING AND SERVICES</span>
    </div>
  </div>

  <p class="when">Jueves, 26 de Noviembre de 2020<br>De 6:30 PM a 10:00 PM</p>

  <p class="agenda">6:30 PM-8:00 PM: Presentación de Plataforma Service Management.<br>8:00 PM-10:00 PM: Cata virtual patrocinada por Montaral &amp; Compañía.</p>

  <p class="rsvp"><strong>RSVP</strong><br>Favor enviar confirmación a<br><strong>ana_veloz@pelvunko.com.do</strong><br>o llamando al<br><strong>(809)-555-0148</strong></p>

  <div class="footer-band"></div>
</main>
</body>
</html>
```